QVLT Meridian LLC Website

Basic website for a start up business in the defense and federal space. If we could have intelligence analysis and technology as a focus that would be great. Looking to use our core colors but a lighter set of web pages would be preferable

Target Market(s)

Defense

Coding

Coded - Design and coding required

Number of Pages Required

3 page

```html
<!DOCTYPE html>
<html lang="en">
<head>
<meta charset="utf-8">
<title>QVLT Meridian LLC — Defense and Federal Space</title>
<link rel="stylesheet" href="https://fonts.googleapis.com/css2?family=Montserrat:wght@400;500;600;700;800&display=swap">
<style>
:root{
  --red:#c8102e;
  --red-bright:#d81440;
  --ink:#1a1a1a;
  --night:#07080c;
  --night-2:#0d1018;
  --paper:#ffffff;
  --mist:#e6e6e6;
  --soft:#cfd3da;
}
*{box-sizing:border-box;margin:0;padding:0}
html,body{width:1200px;height:3278px;overflow:hidden}
body{position:relative;font-family:'Montserrat',sans-serif;color:var(--ink);background:var(--night)}
.abs{position:absolute}
a{color:inherit;text-decoration:none}

/* header */
.site-header{left:0;top:0;width:1200px;height:93px;background:var(--paper)}
.brand{left:132px;top:30px;display:flex;align-items:center;gap:10px;font-weight:700;font-size:22px;letter-spacing:1px;color:var(--ink)}
.brand-dot{width:14px;height:14px;border-radius:50%;background:var(--red)}
.top-phone{left:743px;top:22px;font-size:12px;display:flex;align-items:center;gap:5px;border-bottom:1px solid #333;padding-bottom:2px}
.follow{left:920px;top:22px;font-size:12px;border-bottom:1px solid #333;padding-bottom:2px}
.social-dot{top:20px;width:23px;height:23px;border-radius:50%;background:#111}
.nav{left:0;top:57px;width:1200px;height:22px;font-size:14px;font-weight:500}
.nav a{position:absolute;top:2px;letter-spacing:.3px}
.nav a.active{top:0;left:441px;width:57px;height:22px;background:var(--red);color:#fff;text-align:center;line-height:22px}

/* hero */
.hero{left:0;top:93px;width:1200px;height:541px;
  background:radial-gradient(ellipse 520px 420px at 900px 480px,#2f5f9a 0%,#183256 40%,rgba(10,16,30,0) 75%),
  radial-gradient(circle 120px at 700px 330px,#8a8f98 0%,#3a3e46 55%,rgba(0,0,0,0) 100%),
  linear-gradient(90deg,#05060b 0%,#090b14 55%,#0b1324 100%)}
.hero-title{left:130px;top:178px;font-size:44px;font-weight:800;line-height:44px;color:var(--red-bright)}
.hero-sub{left:132px;top:288px;width:340px;font-size:16px;line-height:20px;color:#fff;font-weight:500}
.btn{background:var(--red);color:#fff;font-weight:600;display:flex;align-items:center;justify-content:center}
.hero-btn{left:132px;top:354px;width:115px;height:36px;font-size:14px}
.dots{left:568px;top:597px;display:flex;gap:6px}
.dots span{width:8px;height:8px;background:#fff}
.dots span.on{background:transparent;border:2px solid var(--red)}

/* feature strip */
.features{left:0;top:634px;width:1200px;height:225px;background:linear-gradient(180deg,#0a0b12,#12131c)}
.feature{top:34px;width:200px;color:#fff}
.feature svg{display:block;height:62px}
.feature h3{margin-top:26px;font-size:14px;font-weight:700;color:var(--red-bright)}
.feature p{margin-top:6px;font-size:12px;line-height:16px;color:#e8e8e8}

/* about */
.about{left:0;top:859px;width:1200px;height:539px;background:var(--paper);overflow:hidden}
.about-photo{left:0;top:0;width:1200px;height:539px;clip-path:polygon(572px 0,1200px 0,1200px 539px,626px 539px);
  background:linear-gradient(180deg,#2c5f99 0%,#5e8bc0 45%,#c9d4e0 72%,#f2efe9 100%)}
.about-stripe{left:0;top:0;width:1200px;height:539px;background:var(--red);clip-path:polygon(557px 0,572px 0,626px 539px,611px 539px)}
.about-title{left:132px;top:44px;font-size:20px;font-weight:800;color:var(--red)}
.rule{height:3px;background:var(--red)}
.about-rule{left:132px;top:79px;width:58px}
.about-text{left:132px;top:111px;width:382px;font-size:13.6px;line-height:19.2px;text-align:justify;color:#333}
.small-btn{left:132px;top:289px;width:77px;height:23px;font-size:9.5px}
.tile{top:354px;width:200px;height:131px;background:radial-gradient(circle at 30% 40%,#1d1f28,#050508);color:#fff;font-weight:800;font-size:14px;text-align:center}
.tile svg{position:absolute;top:22px;left:50%;transform:translateX(-50%)}
.tile span{position:absolute;left:0;right:24px;top:86px}
.tile-a{left:131px;clip-path:polygon(0 0,174px 0,199px 131px,0 131px)}
.tile-b{left:347px;clip-path:polygon(0 0,174px 0,199px 131px,0 131px)}

/* cards */
.cards{left:0;top:1398px;width:1200px;height:445px;background:var(--mist)}
.card{top:42px;width:458px;height:360px;color:#fff}
.card-fed{left:132px;background:radial-gradient(circle 150px at 400px 70px,#3d5a39 0%,#1a2518 50%,rgba(0,0,0,0) 75%),linear-gradient(135deg,#151515 0%,#050505 100%)}
.card-def{left:608px;background:radial-gradient(circle 110px at 120px 140px,#2b5d8c 0%,#0f2d4c 60%,rgba(0,0,0,0) 80%),radial-gradient(circle at 70px 30px,#6cc4ff 0%,rgba(0,0,0,0) 25%),linear-gradient(180deg,#0b2239 0%,#102c4a 70%,#55657a 100%)}
.card-title{font-size:29px;font-weight:800;line-height:29px}
.card p{font-size:12px;line-height:18px;margin-top:10px;color:#eee}
.card .btn{width:83px;height:25px;font-size:10px;margin-top:12px}
.card-fed .card-body{position:absolute;left:233px;top:163px;width:200px}
.card-def .card-body{position:absolute;left:243px;top:50px;width:200px}

/* services */
.services{left:0;top:1843px;width:1200px;height:1435px;background:radial-gradient(ellipse 900px 600px at 600px 300px,#0f1320,#06070b 70%)}
.services-title{left:0;top:55px;width:1200px;text-align:center;font-size:20px;font-weight:800;color:var(--red-bright)}
.services-rule{left:570px;top:92px;width:60px}
.service{top:152px;width:214px;text-align:center;color:#fff}
.service svg{display:block;margin:0 auto;height:80px}
.service h3{margin-top:38px;font-size:16px;font-weight:700}
.service p{margin-top:14px;font-size:12px;line-height:16px;color:#ddd}
.launch-scene{left:0;top:437px;width:1200px;height:700px;
  background:radial-gradient(ellipse 120px 380px at 837px 420px,#d7d9de 0%,#8a7c70 30%,rgba(160,90,30,.45) 55%,rgba(0,0,0,0) 80%),
  radial-gradient(ellipse 900px 260px at 600px 260px,#1b3150 0%,#0d1a2e 45%,rgba(6,7,11,0) 75%)}
.pitch-title{left:134px;top:727px;width:480px;font-size:22px;line-height:28px;font-weight:800;color:var(--red-bright)}
.pitch-text{left:130px;top:836px;width:475px;font-size:17px;line-height:24px;color:#fff}
.pitch-btn{left:131px;top:960px;width:134px;height:39px;font-size:15px}

/* footer */
.footer-brand{left:132px;top:1195px;display:flex;align-items:center;gap:12px;font-weight:700;font-size:30px;letter-spacing:1px;color:#fff}
.footer-col{top:1132px;color:#fff}
.footer-col h4{font-size:13px;font-weight:700;margin-bottom:22px}
.menu-list{list-style:none;font-size:11.5px;line-height:19.8px}
.contact-row{display:flex;gap:12px;align-items:flex-start;font-size:11.5px;line-height:15px;margin-bottom:20px}
.icon-circle{flex:none;width:23px;height:23px;border-radius:50%;background:#fff;display:flex;align-items:center;justify-content:center;margin-top:2px}
.footer-rule{left:133px;top:1345px;width:934px;height:1px;background:#2a2c33}
.copyright{left:0;top:1378px;width:1200px;text-align:center;font-size:9.5px;color:#fff}
</style>
</head>
<body>

<header class="abs site-header">
  <div class="abs brand"><span class="brand-dot"></span>QVLT MERIDIAN</div>
  <div class="abs top-phone">
    <svg width="10" height="10" viewBox="0 0 24 24"><path d="M6.6 10.8a15 15 0 0 0 6.6 6.6l2.2-2.2a1 1 0 0 1 1-.25 11 11 0 0 0 3.6.6 1 1 0 0 1 1 1V20a1 1 0 0 1-1 1A17 17 0 0 1 3 4a1 1 0 0 1 1-1h3.5a1 1 0 0 1 1 1 11 11 0 0 0 .6 3.6 1 1 0 0 1-.25 1z" fill="#222"/></svg>
    +1 888 888 8888
  </div>
  <div class="abs follow">FOLLOW</div>
  <span class="abs social-dot" style="left:987px"></span>
  <span class="abs social-dot" style="left:1015px"></span>
  <span class="abs social-dot" style="left:1043px"></span>
  <nav class="abs nav">
    <a class="active" href="#">HOME</a>
    <a href="#" style="left:529px">ABOUT US</a>
    <a href="#" style="left:636px">DEFENSE</a>
    <a href="#" style="left:741px">FEDERAL SPACE</a>
    <a href="#" style="left:896px">NEWS</a>
    <a href="#" style="left:973px">CONTACT US</a>
  </nav>
</header>

<section class="abs hero" role="img" aria-label="Satellite orbiting above Earth at night with city lights">
</section>
<h1 class="abs hero-title">DEFENSE AND<br>FEDERAL SPACE</h1>
<p class="abs hero-sub">Lorem Ipsum is simply dummy text of the printing and typesetting industry</p>
<a class="abs btn hero-btn" href="#">READ MORE</a>
<div class="abs dots"><span></span><span></span><span class="on"></span><span></span><span></span></div>

<section class="abs features">
  <div class="abs feature" style="left:132px">
    <svg width="62" viewBox="0 0 62 62" fill="none" stroke="var(--red-bright)" stroke-width="4"><circle cx="31" cy="33" r="25"/><circle cx="31" cy="33" r="15"/><circle cx="31" cy="33" r="5" fill="var(--red-bright)"/><path d="M31 33 50 10"/></svg>
    <h3>TRANSPORT</h3>
    <p>Lorem Ipsum is simply dumm y text of the printing and typ esetting industry</p>
  </div>
  <div class="abs feature" style="left:364px">
    <svg width="62" viewBox="0 0 62 62" fill="none" stroke="var(--red-bright)" stroke-width="3"><path d="M10 20a24 24 0 0 0 32 32z"/><path d="M26 36 40 22"/><circle cx="42" cy="20" r="3"/><path d="M48 8a12 12 0 0 1 6 6M46 14a5 5 0 0 1 2 2"/><path d="M6 58h40"/></svg>
    <h3>TRACKING</h3>
    <p>Lorem Ipsum is simply dumm y text of the printing and typ esetting industry</p>
  </div>
  <div class="abs feature" style="left:618px">
    <svg width="62" viewBox="0 0 62 62" fill="none" stroke="var(--red-bright)" stroke-width="3"><rect x="20" y="10" width="34" height="16" transform="rotate(-30 37 18)"/><path d="M8 30l10-6 6 10-10 6z"/><path d="M30 32 22 58M30 32l10 26"/></svg>
    <h3>EMERGING CAPABILITIES</h3>
    <p>Lorem Ipsum is simply dumm y text of the printing and typ esetting industry</p>
  </div>
  <div class="abs feature" style="left:874px">
    <svg width="62" viewBox="0 0 62 62" fill="none" stroke="var(--red-bright)" stroke-width="3"><rect x="24" y="24" width="14" height="14" transform="rotate(45 31 31)"/><rect x="6" y="6" width="16" height="16" transform="rotate(45 14 14)"/><rect x="40" y="40" width="16" height="16" transform="rotate(45 48 48)"/><path d="M20 20l6 6M36 36l6 6"/></svg>
    <h3>SUPPORT</h3>
    <p>Lorem Ipsum is simply dumm y text of the printing and typ esetting industry</p>
  </div>
</section>

<section class="abs about">
  <div class="abs about-photo" role="img" aria-label="Space shuttle lifting off from the launch tower above billowing clouds"></div>
  <div class="abs about-stripe"></div>
  <h2 class="abs about-title">WHO WE ARE</h2>
  <div class="abs rule about-rule"></div>
  <p class="abs about-text">Sed ut perspiciatis unde omnis iste natus error sit voluptatem accusantium doloremque laudantium, totam rem aperiam, eaque ipsa quae ab illo inventore veritatis et quasi architecto beatae vitae dicta sunt explicabo. Nemo enim ipsam voluptatem quia voluptas sit aspernatur aut odit aut fugit, sed quia consequuntur magni dolores eos qui ratione voluptatem sequi nesciunt. Neque porro quisquam est.</p>
  <a class="abs btn small-btn" href="#">READ MORE</a>
  <div class="abs tile tile-a">
    <svg width="40" height="48" viewBox="0 0 40 48" fill="none" stroke="var(--red-bright)" stroke-width="3"><path d="M20 3c7 6 9 15 9 25v8H11v-8c0-10 2-19 9-25z"/><path d="M11 28l-7 8v6h7M29 28l7 8v6h-7"/><path d="M15 44h10"/></svg>
    <span>LOREM IPSUM</span>
  </div>
  <div class="abs tile tile-b">
    <svg width="48" height="48" viewBox="0 0 48 48" fill="none" stroke="var(--red-bright)" stroke-width="3"><path d="M6 20h36a18 18 0 0 1-36 0z"/><path d="M24 20V8"/><circle cx="24" cy="6" r="3"/><path d="M16 44l8-6 8 6"/></svg>
    <span>LOREM IPSUM</span>
  </div>
</section>

<section class="abs cards">
  <article class="abs card card-fed" role="img" aria-label="Communications satellite near a green planet">
    <div class="card-body">
      <h2 class="card-title">FEDERAL<br>SPACE</h2>
      <p>Lorem Ipsum is simply dumm y text of the printing and typ esetting industry</p>
      <a class="btn" href="#">READ MORE</a>
    </div>
  </article>
  <article class="abs card card-def" role="img" aria-label="Ringed blue planet rising over a rocky horizon">
    <div class="card-body">
      <h2 class="card-title">DEFENSE</h2>
      <p>Lorem Ipsum is simply dumm y text of the printing and typ esetting industry</p>
      <a class="btn" href="#">READ MORE</a>
    </div>
  </article>
</section>

<section class="abs services">
  <div class="abs launch-scene" role="img" aria-label="Night side of Earth with a shuttle launching upward"></div>
  <h2 class="abs services-title">OUR SERVICES</h2>
  <div class="abs rule services-rule"></div>

  <div class="abs service" style="left:142px">
    <svg width="80" viewBox="0 0 80 80" fill="none" stroke="var(--red-bright)" stroke-width="3"><circle cx="40" cy="40" r="37"/><circle cx="40" cy="40" r="26"/><circle cx="40" cy="40" r="12" stroke-width="6" stroke-dasharray="5 3"/><circle cx="40" cy="40" r="5"/></svg>
    <h3>LORM IPSUM</h3>
    <p>Sed ut perspiciatis unde omnis iste natus error sit voluptatem accus antium doloremque laudantium, totam rem aperiam.</p>
  </div>
  <div class="abs service" style="left:383px">
    <svg width="80" viewBox="0 0 80 80" fill="none" stroke="var(--red-bright)" stroke-width="3"><path d="M66 10C46 12 32 26 26 44l10 10c18-6 32-20 34-40z"/><circle cx="50" cy="30" r="6"/><path d="M26 44l-12 2 8-14 12-2M36 54l-2 12 14-8 2-12"/><path d="M22 58l-10 10M26 62l-6 8M18 54l-8 6"/></svg>
    <h3>LORM IPSUM</h3>
    <p>Sed ut perspiciatis unde omnis iste natus error sit voluptatem accus antium doloremque laudantium, totam rem aperiam.</p>
  </div>
  <div class="abs service" style="left:618px">
    <svg width="80" viewBox="0 0 80 80" fill="none" stroke="var(--red-bright)" stroke-width="3"><ellipse cx="40" cy="40" rx="36" ry="13"/><ellipse cx="40" cy="40" rx="36" ry="13" transform="rotate(60 40 40)"/><ellipse cx="40" cy="40" rx="36" ry="13" transform="rotate(120 40 40)"/><circle cx="40" cy="40" r="6" fill="var(--red-bright)"/></svg>
    <h3>LORM IPSUM</h3>
    <p>Sed ut perspiciatis unde omnis iste natus error sit voluptatem accus antium doloremque laudantium, totam rem aperiam.</p>
  </div>
  <div class="abs service" style="left:866px">
    <svg width="80" viewBox="0 0 80 80" fill="var(--red-bright)"><path d="M34 2l4 12 12 4-12 4-4 12-4-12-12-4 12-4z"/><path d="M58 26l4 10 10 4-10 4-4 10-4-10-10-4 10-4z"/><path d="M24 44l4 12 12 4-12 4-4 12-4-12-12-4 12-4z"/><circle cx="10" cy="30" r="2"/><circle cx="46" cy="70" r="2"/></svg>
    <h3>LORM IPSUM</h3>
    <p>Sed ut perspiciatis unde omnis iste natus error sit voluptatem accus antium doloremque laudantium, totam rem aperiam.</p>
  </div>

  <h2 class="abs pitch-title">LOREM IPSUM DOLOR SIT AMET CONSECTETUR ADIPISCING ELIT SED DO EIUSMOD TEMPOR</h2>
  <p class="abs pitch-text">There are many variations of passages of Lorem Ipsum available, but the majority have suffered alteration in some form, by injected humour, or randomised words which don't look even slightly believable.</p>
  <a class="abs btn pitch-btn" href="#">CONTACT US</a>

  <div class="abs footer-brand"><span class="brand-dot" style="width:18px;height:18px"></span>QVLT MERIDIAN</div>

  <div class="abs footer-col" style="left:455px">
    <h4>MENU</h4>
    <ul class="menu-list"><li>HOME</li><li>ABOUT US</li><li>DEFENSE</li><li>FEDERAL SPACE</li><li>NEWS</li><li>CONTACT US</li></ul>
  </div>
  <div class="abs footer-col" style="left:652px">
    <h4>CONTACT US</h4>
    <div class="contact-row"><span class="icon-circle"><svg width="10" height="12" viewBox="0 0 24 30"><path d="M12 0a10 10 0 0 0-10 10c0 8 10 20 10 20s10-12 10-20A10 10 0 0 0 12 0zm0 14a4 4 0 1 1 0-8 4 4 0 0 1 0 8z" fill="#2a8ad8"/></svg></span><span>1450 Harbor Point Dr Suite 300<br>Lakeview, FL 32014</span></div>
    <div class="contact-row"><span class="icon-circle"><svg width="10" height="10" viewBox="0 0 24 24"><path d="M6.6 10.8a15 15 0 0 0 6.6 6.6l2.2-2.2a1 1 0 0 1 1-.25 11 11 0 0 0 3.6.6 1 1 0 0 1 1 1V20a1 1 0 0 1-1 1A17 17 0 0 1 3 4a1 1 0 0 1 1-1h3.5a1 1 0 0 1 1 1 11 11 0 0 0 .6 3.6 1 1 0 0 1-.25 1z" fill="#2a8ad8"/></svg></span><span>Call Us<br>+1 888 888 8888</span></div>
    <div class="contact-row"><span class="icon-circle"><svg width="11" height="9" viewBox="0 0 24 18"><rect x="1" y="1" width="22" height="16" rx="2" fill="#2a8ad8"/><path d="M2 2l10 8 10-8" stroke="#fff" stroke-width="2" fill="none"/></svg></span><span>E mail Us<br>info@qvltmeridian.com</span></div>
  </div>
  <div class="abs footer-col" style="left:963px">
    <h4>FOLLOW US</h4>
    <div class="contact-row"><span class="icon-circle"></span><span>Like us on<br>CIRCLEHUB</span></div>
    <div class="contact-row"><span class="icon-circle"></span><span>Follow us on<br>CHIRPLINE</span></div>
    <div class="contact-row"><span class="icon-circle"></span><span>Follow us on<br>WORKLINK</span></div>
  </div>

  <div class="abs footer-rule"></div>
  <p class="abs copyright">Copyright © 2022 All Rights Reserved</p>
</section>

</body>
</html>
```